An anniversary gift for my girlfriend

My girlfriend and I have been dating for almost 2 years. We met online and this has afforded us the really unique opportunity to have the first words we said to each other (the whole conversation, in fact) preserved. We're moving in together in a few months and she doesn't know that I saved the conversation. I've been waiting for this to turn it into something we can hang in our new place.

The only phrase I want to use is:
"Well if you dislike people's knees then I think we'll get along famously"

It's an Nobody Leaves Before Midnight in Portland reference for the curious.

I want the poster to use the words themselves as the art; I'm thinking typography. I'd like it to match her aesthetic, she likes to wear Nora Vell and T. Brisk. Colors shouldn't be anything too "girly". Somewhere I'd like to include the date June 1, 2015. It shouldn't be a major piece of the poster though, just a way to denote the date.

It should fit (and be fully visible in) a 16x20 (inches) frame

Thanks in advance for the work!

Requirements
Must have
• Must use only the words: "Well if you dislike people's knees then I think we'll get along famously"
• I want this to be typography, so making the phrase the center of the poster and the art itself.

```html
<!DOCTYPE html>
<html lang="en">
<head>
<meta charset="utf-8">
<title>Well — Anniversary Poster</title>
<link rel="stylesheet" href="https://fonts.googleapis.com/css2?family=Stardos+Stencil:wght@700&family=Eagle+Lake&family=Fredoka:wght@600&family=Ribeye&family=Holtwood+One+SC&family=Josefin+Sans:wght@400&display=swap">
<style>
  :root {
    --sunshine: #f2ec2a;
    --magenta: #ec008c;
    --peach: #f0a070;
    --ink: #1a1a14;
    --ink-soft: #3a3a20;
    --faint-ornament: rgba(230, 220, 60, 0.55);
    --figure-tone: #d9cf3a;
  }
  * { margin: 0; padding: 0; box-sizing: border-box; }
  html, body {
    width: 960px;
    height: 1200px;
    overflow: hidden;
    background: var(--sunshine);
  }
  .poster {
    position: relative;
    width: 960px;
    height: 1200px;
    background: var(--sunshine);
    overflow: hidden;
  }
  .side-band {
    position: absolute;
    left: 46px;
    top: 0;
    width: 116px;
    height: 1200px;
    background: linear-gradient(180deg, var(--magenta) 0%, var(--magenta) 4%, var(--peach) 14%, var(--magenta) 42%, var(--magenta) 100%);
  }
  .background-ornament {
    position: absolute;
    left: 120px;
    top: 90px;
    width: 780px;
    height: 840px;
    border-radius: 50%;
    background: radial-gradient(ellipse at center, var(--faint-ornament) 0%, rgba(242,236,42,0) 70%);
  }
  .quote {
    position: absolute;
    inset: 0;
    color: var(--ink);
    text-align: center;
  }
  .word-well {
    position: absolute;
    top: 95px;
    left: 0;
    width: 960px;
    display: flex;
    justify-content: center;
    gap: 26px;
    padding-left: 8px;
  }
  .word-well .letter-disc {
    width: 102px;
    height: 102px;
    border-radius: 50%;
    background: var(--ink);
    color: var(--sunshine);
    font-family: "Stardos Stencil", "Impact", sans-serif;
    font-weight: 700;
    font-size: 58px;
    line-height: 102px;
    text-align: center;
  }
  .line {
    position: absolute;
    left: 0;
    width: 960px;
    white-space: nowrap;
  }
  .line-if {
    top: 268px;
    font-family: "Eagle Lake", "Georgia", serif;
    font-size: 46px;
    padding-left: 20px;
  }
  .line-knees {
    top: 398px;
    font-family: "Fredoka", "Arial Rounded MT Bold", sans-serif;
    font-weight: 600;
    font-size: 76px;
    color: var(--ink-soft);
    letter-spacing: 1px;
  }
  .line-then {
    top: 582px;
    font-family: "Ribeye", "Georgia", serif;
    font-size: 44px;
    color: var(--ink-soft);
  }
  .line-famously {
    top: 730px;
    font-family: "Holtwood One SC", "Georgia", serif;
    font-size: 74px;
    color: var(--ink);
    letter-spacing: 2px;
    text-shadow: 3px 3px 0 var(--sunshine), 5px 5px 0 var(--ink);
  }
  .figures {
    position: absolute;
    left: 156px;
    top: 917px;
    width: 650px;
    height: 166px;
    border-radius: 70px;
    background: linear-gradient(90deg, var(--figure-tone), #e8dd3a 50%, var(--figure-tone));
  }
  .date {
    position: absolute;
    right: 30px;
    top: 1144px;
    font-family: "Josefin Sans", "Helvetica", sans-serif;
    font-size: 19px;
    color: var(--ink);
    letter-spacing: 1px;
  }
</style>
</head>
<body>
  <main class="poster">
    <div class="side-band" role="img" aria-label="Vertical magenta band with a distressed peach paint texture"></div>
    <div class="background-ornament" role="img" aria-label="Faint swirling leaf ornament behind the lettering"></div>

    <section class="quote">
      <h1 class="word-well" aria-label="Well">
        <span class="letter-disc">W</span>
        <span class="letter-disc">E</span>
        <span class="letter-disc">L</span>
        <span class="letter-disc">L</span>
      </h1>
      <p class="line line-if">if you dislike</p>
      <p class="line line-knees">people’s knees</p>
      <p class="line line-then">then I think we'll get along</p>
      <p class="line line-famously">FAMOUSLY</p>
    </section>

    <div class="figures" role="img" aria-label="Row of five minimalist character head silhouettes"></div>

    <p class="date">June 1, 2015</p>
  </main>
</body>
</html>
```